Midnight Lanterns - Falling to Rise Reading the Hidden Grammar of Sleep

Book Title:
Midnight Lanterns
Falling to Rise

Reading the Hidden Grammar of Sleep

by Greta Vonhalm

tells the story of how dreams transform us, bringing the wisdom of our mind, body and spirit to us in our dreams. We have nerves coming into our brain from every part of our body relaying psychological and physiological information within us and it is revealed in our dream narrative.Once you understand the symbolic, visual language of dreams, you will find out/understand what is going on within. After all the dream is always about the dreamer. Yes, it is all about you!

Target Market(s)

Anyone who dreams, that includes all of us

Font styles to use
Serif

Colors
ec1f27
f37122
0692cd

Requirements
Must have
• Use this image please with Shadowed serif type font, in the color pallette
• I would like images for the cover to reflect being reborn for example - a phoenix. Dying in a dream is always a symbolic gesture/metaphor of profound psychological spiritual change, and the way the person dies is symbolic too. It's important that the image on the front reflects that.
Nice to have
• A good visual on the cover helps, just like they do in a dream since the language of the dream is symbols, metaphor, colors portray emotions. We respond to images because we only had images before our written language

```html
<!DOCTYPE html>
<html lang="en">
<head>
<meta charset="utf-8">
<title>Midnight Lanterns – Falling to Rise</title>
<link rel="stylesheet" href="https://fonts.googleapis.com/css2?family=Cinzel:wght@600;700;900&display=swap">
<style>
  :root {
    --sky-teal: #2a8fa8;
    --sky-blue: #0692cd;
    --sky-deep: #1d5f7a;
    --flame-red: #ec1f27;
    --flame-orange: #f37122;
    --flame-gold: #f6b233;
    --ember-dark: #5a1a0c;
    --title-gold: #f4d21a;
    --subtitle-white: #fdf6e8;
    --author-cream: #f8e6b8;
    --shadow-ink: rgba(20, 10, 5, 0.85);
  }
  html, body {
    margin: 0;
    padding: 0;
    overflow: hidden;
    background: #1a1a1a;
  }
  .cover {
    position: relative;
    width: 800px;
    height: 1200px;
    overflow: hidden;
    font-family: "Cinzel", "Times New Roman", serif;
    text-align: center;
  }
  .cover-art {
    position: absolute;
    inset: 0;
    background:
      radial-gradient(ellipse 46% 30% at 50% 48%, var(--flame-gold) 0%, var(--flame-orange) 40%, rgba(236,31,39,0.85) 70%, rgba(236,31,39,0) 100%),
      radial-gradient(ellipse 80% 28% at 50% 92%, var(--flame-orange) 0%, var(--flame-red) 45%, rgba(90,26,12,0) 100%),
      linear-gradient(180deg, var(--sky-teal) 0%, var(--sky-blue) 22%, var(--sky-deep) 45%, var(--ember-dark) 78%, #2a0c06 100%);
  }
  .title-block {
    position: absolute;
    top: 44px;
    left: 0;
    right: 0;
  }
  .series-title,
  .main-title {
    margin: 0;
    color: var(--title-gold);
    font-weight: 700;
    line-height: 1;
    text-shadow: 3px 4px 4px var(--shadow-ink), 0 0 10px rgba(0,0,0,0.35);
  }
  .series-title {
    font-size: 70px;
    letter-spacing: 2px;
  }
  .main-title {
    font-size: 96px;
    letter-spacing: 2px;
    margin-top: 8px;
  }
  .tagline {
    margin: 22px 0 0;
    color: var(--flame-orange);
    font-size: 64px;
    font-weight: 700;
    line-height: 1;
    letter-spacing: 1px;
    text-shadow: 3px 4px 4px var(--shadow-ink);
  }
  .subtitle {
    margin: 26px 0 0;
    color: var(--subtitle-white);
    font-size: 29px;
    font-weight: 600;
    line-height: 1.3;
    letter-spacing: 0.5px;
    text-shadow: 2px 3px 3px var(--shadow-ink);
  }
  .author {
    position: absolute;
    left: 0;
    right: 0;
    bottom: 44px;
    margin: 0;
    color: var(--author-cream);
    font-size: 62px;
    font-weight: 700;
    letter-spacing: 3px;
    line-height: 1;
    text-shadow: 3px 4px 4px var(--shadow-ink);
  }
</style>
</head>
<body>
  <main class="cover">
    <div class="cover-art" role="img" aria-label="A fiery phoenix with outstretched wings rising from flames beneath a stormy teal sky"></div>
    <header class="title-block">
      <h1 class="series-title">MIDNIGHT LANTERNS</h1>
      <p class="tagline">FALLING TO RISE</p>
      <p class="subtitle">READING<br>THE HIDDEN GRAMMAR OF SLEEP</p>
    </header>
    <p class="author">GRETA VONHALM</p>
  </main>
</body>
</html>
```